Harrowgate Supply Group Business Card Design

The Business Card will be one side only with Harrowgate Supplies Group Logo
Card should have:
Name
Title
Office phone Number
Cell Number
email address
Website
Street Address
Our Slogan is Rugged and Reliable
Looking for something that stands out from other business cards

Target Market(s)

Heavy equipment Lease Company

```html
<!DOCTYPE html>
<html lang="en">
<head>
<meta charset="utf-8">
<title>Harrowgate Supplies Group – Business Card</title>
<link href="https://fonts.googleapis.com/css2?family=Lato:ital,wght@0,400;0,700;0,900;1,700;1,900&display=swap" rel="stylesheet">
<style>
  :root {
    --navy: #27297a;
    --red: #d21a33;
    --card-white: #f8f8f8;
    --page-bg: #e6e6e6;
    --text-light: #ffffff;
  }
  html, body {
    margin: 0;
    padding: 0;
    width: 1200px;
    height: 870px;
    overflow: hidden;
    background: var(--page-bg);
  }
  .business-card {
    position: absolute;
    left: 50px;
    top: 121px;
    width: 800px;
    height: 457px;
    transform: scale(1.375);
    transform-origin: top left;
    background: var(--card-white);
    box-shadow: 0 2px 6px rgba(0,0,0,0.25);
    overflow: hidden;
    font-family: "Lato", Arial, sans-serif;
  }
  .card-shapes {
    position: absolute;
    inset: 0;
    width: 800px;
    height: 457px;
  }
  .brand {
    position: absolute;
    left: 57px;
    top: 44px;
    display: flex;
    align-items: center;
    gap: 14px;
  }
  .brand-dot {
    width: 54px;
    height: 54px;
    border-radius: 50%;
    background: var(--navy);
  }
  .brand-name {
    font-weight: 900;
    font-size: 23px;
    line-height: 1;
    color: var(--red);
    letter-spacing: 0.2px;
    margin: 0;
  }
  .person {
    position: absolute;
    left: 59px;
    top: 196px;
  }
  .person-name {
    margin: 0;
    font-weight: 900;
    font-size: 28px;
    line-height: 1;
    color: var(--navy);
  }
  .person-title {
    margin: 3px 0 0;
    font-weight: 400;
    font-size: 19px;
    line-height: 1.1;
    color: var(--red);
  }
  .contact {
    position: absolute;
    right: 62px;
    top: 205px;
    text-align: right;
    color: var(--text-light);
    font-size: 17px;
    line-height: 1.35;
  }
  .address {
    margin: 0 0 10px;
    font-style: normal;
  }
  .contact-list {
    list-style: none;
    margin: 0;
    padding: 0;
  }
  .contact-item {
    display: flex;
    justify-content: flex-end;
    align-items: center;
    gap: 9px;
    font-size: 16.5px;
    line-height: 25px;
  }
  .contact-icon {
    width: 16px;
    height: 16px;
    flex: none;
    fill: var(--red);
  }
  .slogan {
    margin: 14px 0 0;
    font-weight: 900;
    font-style: italic;
    font-size: 19px;
    color: var(--red);
  }
</style>
</head>
<body>
  <div class="business-card">
    <svg class="card-shapes" viewBox="0 0 800 457" aria-hidden="true">
      <polygon fill="var(--navy)" points="736,0 800,0 800,457 0,457 0,316 152,433"/>
      <polyline fill="none" stroke="#ffffff" stroke-width="2" points="0,312 152,429 730,0"/>
      <polyline fill="none" stroke="var(--red)" stroke-width="5" points="0,306 152,424 723,0"/>
    </svg>

    <div class="brand">
      <span class="brand-dot"></span>
      <p class="brand-name">HARROWGATE SUPPLIES GROUP</p>
    </div>

    <div class="person">
      <h1 class="person-name">DANIEL REEVES</h1>
      <p class="person-title">CEO/FOUNDER</p>
    </div>

    <div class="contact">
      <address class="address">4120 Birchwood Road<br>Fairbanks, Alaska 99701</address>
      <ul class="contact-list">
        <li class="contact-item">555 214 0187
          <svg class="contact-icon" viewBox="0 0 16 16" aria-hidden="true"><path d="M3.6 1.2l2.3 2.6c.3.4.3.9 0 1.3L4.7 6.4c.8 1.9 2.9 4 4.9 4.9l1.3-1.2c.4-.3.9-.3 1.3 0l2.6 2.3c.4.4.4 1 0 1.4l-1.3 1.3C11.4 17 0 5.6 1 3.3l1.2-2.1c.4-.4 1-.4 1.4 0z"/></svg>
        </li>
        <li class="contact-item">555 382 6410
          <svg class="contact-icon" viewBox="0 0 16 16" aria-hidden="true"><path d="M4.5 0h7c.8 0 1.5.7 1.5 1.5v13c0 .8-.7 1.5-1.5 1.5h-7C3.7 16 3 15.3 3 14.5v-13C3 .7 3.7 0 4.5 0zm.3 2v10.5h6.4V2H4.8zM8 13.3a.9.9 0 1 0 0 1.8.9.9 0 0 0 0-1.8z"/></svg>
        </li>
        <li class="contact-item">daniel@harrowgatesupplies.com
          <svg class="contact-icon" viewBox="0 0 16 16" aria-hidden="true"><path d="M1 3.5h14v1.2L8 9 1 4.7z M1 6.2l7 4.3 7-4.3V12.5H1z"/></svg>
        </li>
        <li class="contact-item">harrowgatesupplies.com
          <svg class="contact-icon" viewBox="0 0 16 16" aria-hidden="true"><path d="M8 0a8 8 0 1 0 0 16A8 8 0 0 0 8 0zm-1 2.2c-.6.8-1.6 1.2-2 2.3.9.6 2 .3 2.6 1.2.4.7-.5 1.4-.2 2.2.4 1 1.8.8 2.1 1.9.3 1-.6 2.2-.1 3.5a6.1 6.1 0 0 1-7.3-6A6 6 0 0 1 7 2.2zm3.5.5a6 6 0 0 1 3.2 6.6c-.6-.5-1-1.4-1.9-1.5-.8-.1-1.5.6-2.2.2-.7-.5-.2-1.6.4-2.1.6-.6 1.5-.7 1.4-1.6-.1-.7-.8-1-.9-1.6z"/></svg>
        </li>
      </ul>
      <p class="slogan">Rugged &amp; Reliable</p>
    </div>
  </div>
</body>
</html>
```